Wine Bottle Lable

Want a unique, simple but elegant, label for a wine bottle. I want to use the letters "TWG" in the design which is a moniker for my last name "Tallwidge". The letters TWG do not have to be juxtaposed together so that it is recognizable, or they could be something like T-WG, WG-T, TGW T-WG-T, etc. The X could be totally separated from the NO, or otherwise. The wine is a white wine in a clear bottle. I need Adobe Illustrator files so I can add the wine varietal, year, alcohol content. The label should be 4" wide and 5" tall.

Colors

Designer to choose colors to be used in the design.

Requirements
Nice to have
• outstanding but simple graphics

```html
<!DOCTYPE html>
<html lang="en">
<head>
<meta charset="utf-8">
<title>Tallwidge TWG 1992 – Wine Label</title>
<link rel="stylesheet" href="https://fonts.googleapis.com/css2?family=Antonio:wght@400;600&family=Oswald:wght@600&family=Zilla+Slab:wght@700&display=swap">
<style>
  :root {
    --ink: #0a0214;
    --paper: #ffffff;
  }
  * { margin: 0; padding: 0; box-sizing: border-box; }
  html, body {
    width: 960px;
    height: 1200px;
    overflow: hidden;
    background: var(--paper);
  }
  .label {
    position: relative;
    width: 960px;
    height: 1200px;
    background: var(--paper);
    color: var(--paper);
  }
  .label__panel {
    position: absolute;
    left: 48px;
    top: 48px;
    width: 864px;
    height: 959px;
    background: var(--ink);
  }
  .corner {
    position: absolute;
    width: 107px;
    height: 107px;
  }
  .corner svg { display: block; width: 100%; height: 100%; }
  .corner--tl { left: 23px;  top: 23px; }
  .corner--tr { right: 23px; top: 23px; }
  .corner--bl { left: 23px;  bottom: 23px; }
  .corner--br { right: 23px; bottom: 23px; }

  .brand {
    position: absolute;
    left: 0;
    right: 0;
    top: 148px;
    text-align: center;
    font-family: "Oswald", sans-serif;
    font-weight: 600;
    font-size: 100px;
    line-height: 1;
    letter-spacing: 1px;
  }
  .monogram {
    position: absolute;
    left: 157px;
    top: 358px;
    width: 550px;
    height: 270px;
    display: flex;
    justify-content: space-between;
    align-items: center;
    font-family: "Antonio", sans-serif;
    font-weight: 400;
    font-size: 318px;
    line-height: 1;
  }
  .monogram span {
    display: block;
    width: 100px;
    text-align: center;
  }
  .vintage {
    position: absolute;
    left: 0;
    right: 0;
    top: 734px;
    text-align: center;
    font-family: "Antonio", sans-serif;
    font-weight: 400;
    font-size: 100px;
    line-height: 1;
    letter-spacing: 38px;
    text-indent: 38px;
  }
  .label__band {
    position: absolute;
    left: 0;
    right: 0;
    top: 1055px;
    height: 145px;
    background: var(--ink);
    display: flex;
    justify-content: space-between;
    align-items: center;
    padding: 4px 54px 0 66px;
    font-family: "Zilla Slab", serif;
    font-weight: 700;
    font-size: 62px;
    line-height: 1;
  }
</style>
</head>
<body>
  <main class="label">
    <section class="label__panel">
      <div class="corner corner--tl" role="img" aria-label="Leaf ornament, top left corner">
        <svg viewBox="0 0 100 100"><defs><radialGradient id="orn" cx="50%" cy="50%" r="50%"><stop offset="0" stop-color="#ffffff"/><stop offset="1" stop-color="#0a0214"/></radialGradient></defs><rect width="100" height="100" fill="url(#orn)"/></svg>
      </div>
      <div class="corner corner--tr" role="img" aria-label="Leaf ornament, top right corner">
        <svg viewBox="0 0 100 100"><rect width="100" height="100" fill="url(#orn)"/></svg>
      </div>
      <div class="corner corner--bl" role="img" aria-label="Leaf ornament, bottom left corner">
        <svg viewBox="0 0 100 100"><rect width="100" height="100" fill="url(#orn)"/></svg>
      </div>
      <div class="corner corner--br" role="img" aria-label="Leaf ornament, bottom right corner">
        <svg viewBox="0 0 100 100"><rect width="100" height="100" fill="url(#orn)"/></svg>
      </div>

      <h1 class="brand">Tallwidge</h1>
      <p class="monogram" aria-label="TWG"><span>T</span><span>W</span><span>G</span></p>
      <p class="vintage">1992</p>
    </section>

    <footer class="label__band">
      <span class="volume">750ml</span>
      <span class="abv">Alc. 14.5% VOL</span>
    </footer>
  </main>
</body>
</html>
```